Computer consultant business card

Brimlo Software is a newly started computer consulting company. It's a small one-man company that provides mostly Velunix applications but also websites in collaboration with designers. I'm running this company on the side of full time university studies.

I want the final design to be clean and memorable. Be creative! :)

Some inspiration:
http://www.tavelpix.net/design/73519
http://www.tavelpix.net/design/2739566/business-card-design-by-quillbop
http://www.tavelpix.net/design/804613/business-card-design-by-lorvena-brukwaldsen

See attachment for my company logo.
Updates

I would like to thank everyone for submitting! I'll need a couple of days to review and ultimately select a design.

Target Market(s)

Non-technical entrepreneurs and small companies.

Industry/Entity Type

University

Requirements
Must have
• My company logo.
In any way, both colors from my logo.
First- and last name, e-mail and phone number.
Double-sided design.
Nice to have
• Something creative with the symbol in my logo

```html
<!DOCTYPE html>
<html lang="en">
<head>
<meta charset="utf-8">
<title>Brimlo Software – Business Card</title>
<link rel="stylesheet" href="https://fonts.googleapis.com/css2?family=Quicksand:wght@500;600;700&display=swap">
<style>
  :root {
    --white: #fcfdfd;
    --yellow-light: #ffd83c;
    --yellow-main: #fdcb00;
    --ink: #333335;
    --blue: #2b7cff;
  }
  * { margin: 0; padding: 0; box-sizing: border-box; }
  html, body {
    width: 1200px;
    height: 741px;
    overflow: hidden;
    background: var(--white);
  }
  .card {
    position: relative;
    width: 1200px;
    height: 741px;
    overflow: hidden;
    font-family: "Quicksand", sans-serif;
    color: var(--ink);
  }
  .card__background {
    position: absolute;
    inset: 0;
  }
  .brand {
    position: absolute;
    left: 44px;
    top: 268px;
    display: flex;
    align-items: center;
    gap: 26px;
  }
  .brand__dot {
    width: 120px;
    height: 120px;
    border-radius: 50%;
    background: var(--blue);
  }
  .brand__name {
    font-size: 96px;
    font-weight: 700;
    color: var(--ink);
    letter-spacing: 1px;
    line-height: 1;
  }
  .holder-name {
    position: absolute;
    left: 42px;
    top: 428px;
    font-size: 52px;
    font-weight: 500;
    color: var(--blue);
    line-height: 1.1;
  }
  .contact {
    position: absolute;
    right: 26px;
    top: 676px;
    display: flex;
    align-items: center;
    gap: 14px;
    font-size: 31px;
    font-weight: 600;
    color: #141414;
  }
  .contact__item {
    display: flex;
    align-items: center;
    gap: 12px;
  }
  .contact__icon { display: block; }
  .contact__divider {
    width: 5px;
    height: 44px;
    background: #2a2a2a;
    margin: 0 18px;
  }
</style>
</head>
<body>
  <div class="card">
    <svg class="card__background" width="1200" height="741" viewBox="0 0 1200 741" aria-hidden="true">
      <rect width="1200" height="741" fill="var(--yellow-light)"/>
      <path d="M320,0 C470,70 585,230 560,410 C540,550 460,650 390,741 L1200,741 L1200,345 C1010,160 720,40 420,0 Z" fill="var(--yellow-main)"/>
      <path d="M0,0 L268,0 C430,80 520,220 510,370 C500,520 400,650 266,741 L0,741 Z" fill="var(--white)"/>
    </svg>

    <div class="brand">
      <span class="brand__dot"></span>
      <span class="brand__name">brimlo</span>
    </div>

    <p class="holder-name">Name Surname</p>

    <div class="contact">
      <span class="contact__item">
        <svg class="contact__icon" width="42" height="42" viewBox="0 0 42 42" aria-hidden="true">
          <circle cx="21" cy="21" r="18.5" fill="none" stroke="#141414" stroke-width="3"/>
          <path d="M14 11 l5 0 l2 6 l-3 2.5 c1.5 3 3.5 5 6.5 6.5 l2.5 -3 l6 2 l0 5 c-1 1 -3 1.5 -5 1 c-7 -2 -13 -8 -15 -15 c-0.5 -2 0 -4 1 -5 z" fill="#141414"/>
        </svg>
        <span>Call: (123) 456 7890</span>
      </span>
      <span class="contact__divider"></span>
      <span class="contact__item">
        <svg class="contact__icon" width="48" height="32" viewBox="0 0 48 32" aria-hidden="true">
          <rect x="0" y="0" width="48" height="32" fill="#141414"/>
          <path d="M2 2 L24 18 L46 2" fill="none" stroke="var(--yellow-main)" stroke-width="2.5"/>
          <path d="M2 30 L18 14 M46 30 L30 14" fill="none" stroke="var(--yellow-main)" stroke-width="2"/>
        </svg>
        <span>email hello@brimlo.net</span>
      </span>
    </div>
  </div>
</body>
</html>
```